New Year Resolution Infographic

We are a weight loss company that provides holistic, natural nutrition programs to consumers -- you can see our Web site at www.TrimLark.com We need a simple infographic to be shared on social media and via email for New Year's day. The topic for the infographic is "how to set and keep your weight loss resolution". We've outlined 5 process steps for consumers to follow to assist with their weight loss resolutions, and we would like to depict this graphically.

Target Market(s)

Women age 35-65 who are planning to make a resolution to lose weight in the new year.

Industry/Entity Type

Health And Wellness

Font styles to use
Sans Serif

Colors
0392cd
9bcb3c

Requirements
Must have
• Initial graphic showing failure stats (see copy)
• Graphic showing process steps in making/keeping a resolution (see copy)
• TrimLark Logo

```html
<!DOCTYPE html>
<html lang="en">
<head>
<meta charset="utf-8">
<title>TrimLark – How to Set and Reach Your Weight Loss Resolution</title>
<link href="https://fonts.googleapis.com/css2?family=Montserrat:wght@300;400;500;700;800&display=swap" rel="stylesheet">
<style>
  :root {
    --brand-blue: #0392cd;
    --sky-blue: #1fa9e1;
    --brand-green: #9bcb3c;
    --leaf-green: #8db33a;
    --ring-grey: #454545;
    --ink: #3a3a3a;
    --step-reflect: #ee5a2c;
    --step-resolve: #1fa9e1;
    --step-replace: #8db33a;
    --step-record: #f8ab3a;
    --step-reward: #2c2c2c;
    --paper: #ffffff;
  }
  * { margin: 0; padding: 0; box-sizing: border-box; }
  html, body { width: 908px; height: 1200px; overflow: hidden; background: var(--paper); }
  body { font-family: "Montserrat", Arial, sans-serif; color: var(--ink); }

  .poster { position: relative; width: 908px; height: 1200px; overflow: hidden; background: var(--paper); }

  .wave-backdrop {
    position: absolute; left: -60px; top: 0; width: 360px; height: 1200px;
    background: linear-gradient(100deg, rgba(155,203,60,0.28) 0%, rgba(31,169,225,0.16) 35%, rgba(255,255,255,0) 70%);
    transform: skewX(-8deg);
  }

  .brand { position: absolute; left: 330px; top: 62px; display: flex; align-items: center; gap: 18px; }
  .brand-dot { width: 64px; height: 64px; border-radius: 50%; background: var(--brand-green); }
  .brand-name { font-size: 64px; font-weight: 500; color: var(--sky-blue); letter-spacing: -1px; line-height: 1; }

  .intro { position: absolute; left: 40px; top: 188px; width: 840px; font-size: 24.5px; font-weight: 400; line-height: 33px; }

  .diagram { position: absolute; left: 0; top: 0; width: 908px; height: 1200px; }

  .hub-title { position: absolute; left: 283px; top: 500px; width: 320px; text-align: center; line-height: 1; }
  .hub-title .light { display: block; color: var(--leaf-green); font-weight: 300; }
  .hub-title .bold { display: block; color: var(--sky-blue); font-weight: 800; }
  .hub-title .small { font-size: 29px; margin-bottom: 6px; }
  .hub-title .big { font-size: 40px; margin-bottom: 4px; }

  .step-label {
    position: absolute; height: 53px; display: flex; align-items: stretch; background: var(--paper);
    box-shadow: 4px 5px 6px rgba(0,0,0,0.12);
  }
  .step-num { width: 54px; display: flex; align-items: center; justify-content: center; color: #fff; font-size: 34px; font-weight: 800; letter-spacing: -1px; }
  .step-word { display: flex; align-items: center; padding: 0 12px 0 8px; font-size: 26px; font-weight: 800; letter-spacing: 0.5px; }

  .reflect .step-num { background: var(--step-reflect); } .reflect .step-word { color: var(--step-reflect); }
  .resolve .step-num { background: var(--step-resolve); } .resolve .step-word { color: var(--step-resolve); }
  .replace .step-num { background: var(--step-replace); } .replace .step-word { color: var(--step-replace); }
  .record .step-num { background: var(--step-record); } .record .step-word { color: var(--step-record); }
  .reward .step-num { background: var(--step-reward); } .reward .step-word { color: var(--step-reward); }

  .step-text { position: absolute; font-size: 16.5px; font-weight: 400; line-height: 22.3px; color: #555; }

  .closing { position: absolute; left: 62px; top: 984px; width: 790px; font-size: 24.5px; line-height: 33px; font-weight: 400; }
  .site-url { position: absolute; right: 99px; top: 1126px; font-size: 41px; font-weight: 300; color: var(--sky-blue); }
</style>
</head>
<body>
<main class="poster">
  <div class="wave-backdrop" role="img" aria-label="Soft flowing green and blue wave lines"></div>

  <header class="brand">
    <span class="brand-dot"></span>
    <span class="brand-name">TRIMLARK</span>
  </header>

  <p class="intro">Weight loss is the #1 New Year resolution, but we know that resolutions are very difficult to keep. While 45% of Americans make New Year resolutions, only 8% succeed in keeping them. Here is a quick guide to setting and reaching your weight loss resolution this year.</p>

  <svg class="diagram" viewBox="0 0 908 1200" aria-hidden="true">
    <circle cx="443" cy="574" r="184" fill="none" stroke="var(--ring-grey)" stroke-width="18"/>
    <line x1="242" y1="400" x2="283" y2="471" stroke="var(--step-reflect)" stroke-width="3"/>
    <line x1="640" y1="404" x2="607" y2="473" stroke="var(--step-reward)" stroke-width="3"/>
    <line x1="248" y1="739" x2="281" y2="675" stroke="var(--step-resolve)" stroke-width="3"/>
    <line x1="632" y1="731" x2="607" y2="677" stroke="var(--step-record)" stroke-width="3"/>
    <line x1="443" y1="765" x2="443" y2="783" stroke="var(--step-replace)" stroke-width="3"/>
    <circle cx="290" cy="485" r="14" fill="#fff" stroke="var(--step-reflect)" stroke-width="5"/>
    <circle cx="596" cy="485" r="14" fill="#fff" stroke="var(--step-reward)" stroke-width="5"/>
    <circle cx="290" cy="661" r="14" fill="#fff" stroke="var(--step-resolve)" stroke-width="5"/>
    <circle cx="596" cy="662" r="14" fill="#fff" stroke="var(--step-record)" stroke-width="5"/>
    <circle cx="443" cy="749" r="14" fill="#fff" stroke="var(--step-replace)" stroke-width="5"/>
  </svg>

  <h1 class="hub-title">
    <span class="light small">HOW TO SET AND</span>
    <span class="bold big">REACH YOUR</span>
    <span class="light big">WEIGHT LOSS</span>
    <span class="bold big">RESOLUTION</span>
  </h1>

  <div class="step-label reflect" style="left:40px;top:376px;width:202px"><span class="step-num">01</span><span class="step-word">REFLECT</span></div>
  <p class="step-text" style="left:42px;top:450px;width:215px">Get clear on why the achievement of your resolution is important. You'll need to come back to this if you falter!</p>

  <div class="step-label resolve" style="left:46px;top:715px;width:200px"><span class="step-num">02</span><span class="step-word">RESOLVE</span></div>
  <p class="step-text" style="left:40px;top:795px;width:265px">Set a weight loss goal for the year that is realistic, then break this up into even shorter term goals of 30-60 days, with a specific diet and activity plan to guide you.</p>

  <div class="step-label replace" style="left:333px;top:783px;width:198px"><span class="step-num">03</span><span class="step-word">REPLACE</span></div>
  <p class="step-text" style="left:329px;top:864px;width:270px">Clear out your pantry and stock up with only healthy foods. Then work to build new activity and eating habits that take the place of your current habits.</p>

  <div class="step-label record" style="left:632px;top:715px;width:195px"><span class="step-num">04</span><span class="step-word">RECORD</span></div>
  <p class="step-text" style="left:628px;top:802px;width:260px">Track your progress daily, tell your family and friends about your resolution to create more accountability, and recruit a partner to share your journey.</p>

  <div class="step-label reward" style="left:640px;top:374px;width:190px"><span class="step-num">05</span><span class="step-word">REWARD</span></div>
  <p class="step-text" style="left:637px;top:444px;width:240px">Rather than using unhealthy food as a reward or cheat, give yourself healthy or relaxing experiences – such as a spa treatment or taking a new fitness class.</p>

  <p class="closing">TrimLark can help you achieve your weight loss resolution in the New Year. We invite you to learn more and contact us for a free consultation.</p>
  <p class="site-url">www.trimlark.com</p>
</main>
</body>
</html>
```